Fatigued and Overloaded by COVID Messages? We need original illustrations to show that.

Everywhere you look there are messages about COVID. That is leading many people to feel fatigued and overloaded by the messages.

We surveyed U.S. adults March 20th - 24th, 2020 and measured message fatigue, information overload, perceived repetition, and perceived exaggeration. Here is how participants responded:

When it comes to coronavirus . . .
55% feel exhausted by all the messages.
54% feel overloaded by the amount of information.
51% feel that the messages are repetitive.
47% feel like messages exaggerate how bad it is.

In other words, almost half of U.S. adults show signs of message fatigue, information overload, perceived message repetition, and perceived message exaggeration.

We will continue to survey 400 adults every week for the next 16 weeks. Each time we will measure message fatigue, information overload, perceived repetition, and perceived exaggeration. We expect that it will increase over time.

What are we looking for? We need innovative and original illustrations that attempt to communicate these findings. The illustrations would visualize message fatigue, information overload, perceived message repetition, and perceived message exaggeration.

What sort of visual are we looking for? Our preference is for an original illustration (or set of illustrations). Our preference is for creative and powerful illustrations, but we are also open to the creative and well-executed infographics.

We need these images fast . We will award monetary prizes to the 3 best designs. If we like more than that, then we might purchase more (e.g., in past contests, we have purchased as many as 30 designs).

What we will need:
(1) The illustrations must be original and we will need the photoshop and/or illustrator files for all artwork. (By original, we mean that the illustrations are 100% created by you. Our organization requires that we utilize only original illustrated work. We have had issues with free imagery being pirated and reposted as free. We sidestep that issue by just having everything created.)

(2) The illustration should say, somewhere: "Based on a survey of 400 U.S. adults conducted March 20 - 24th, 2020."

(3) We will have almost 4 months worth of data by the time this is done. In other words, the illustrations might be able to help us present that weekly data.

(4) We have conducted other Artvendo projects. It might be helpful to examine designs we liked in the past. For example, here is another COVID project we just finished:

https://jobs.artvendo-example.com/job/5162048

Target Market(s)

U.S. adults

Requirements
Must have
• Original illustrations. Mobile friendly design. People will view this on their smartphones.
Nice to have
• A design that we can use to communicate the data across time.

```html
<!DOCTYPE html>
<html lang="en">
<head>
<meta charset="utf-8">
<title>Fatigued and Overloaded by COVID Messages</title>
<link rel="stylesheet" href="https://fonts.googleapis.com/css2?family=Macondo&display=swap">
<style>
  :root {
    --yellow: #f2e72a;
    --red: #ec1e2b;
    --blue: #175a8b;
    --ink: #000000;
    --paper: #ffffff;
    --olive: #c9bd3a;
  }
  * { margin: 0; padding: 0; box-sizing: border-box; }
  html, body { width: 713px; height: 1200px; overflow: hidden; background: var(--yellow); }
  body { font-family: "Macondo", cursive; color: var(--ink); }
  .poster { position: relative; width: 713px; height: 1200px; background: var(--yellow); overflow: hidden; }

  .title-band {
    position: absolute; left: 21px; top: 21px; width: 663px; height: 132px;
    background: var(--ink); color: var(--paper); text-align: center;
  }
  .title {
    font-weight: 400; font-size: 44px; line-height: 50px; padding-top: 14px; letter-spacing: 1px;
  }
  .virus-icon { position: absolute; border-radius: 50%; }
  .virus-icon.white-left { left: 35px; top: 75px; width: 52px; height: 46px; background: var(--paper); }
  .virus-icon.white-right { left: 620px; top: 30px; width: 42px; height: 38px; background: var(--paper); }
  .virus-icon.yellow-right { left: 580px; top: 80px; width: 64px; height: 58px; background: var(--yellow); }

  .section-label {
    position: absolute; left: 110px; top: 175px; width: 489px; height: 64px;
    background: var(--ink); color: var(--paper);
    font-size: 34px; line-height: 64px; text-align: center; letter-spacing: 3px;
  }

  .figure-art {
    position: absolute; left: 61px; top: 253px; width: 190px; height: 146px;
    background: linear-gradient(160deg, #e9a66d 0%, #ec1e2b 70%);
    border-radius: 40% 50% 20% 30%;
  }

  .stat { position: absolute; }
  .bar {
    position: absolute; height: 46px; border: 5px solid var(--ink);
    box-shadow: 3px 3px 0 var(--ink); display: flex; overflow: hidden;
  }
  .bar .fill { background: var(--yellow); height: 100%; display: flex; align-items: center; justify-content: center; }
  .bar .rest { flex: 1; height: 100%; }
  .bar.red-track .rest { background: var(--red); }
  .bar.blue-track .rest { background: var(--blue); }
  .percent { font-size: 30px; font-weight: 400; }
  .red-track .percent { color: var(--blue); }
  .blue-track .percent { color: var(--red); }
  .stat-label {
    position: absolute; font-size: 26px; line-height: 30px; text-align: center;
    letter-spacing: 2px; white-space: nowrap;
  }

  .summary {
    position: absolute; left: 14px; top: 930px; width: 681px; height: 97px;
    background: var(--red); color: var(--paper); text-align: center;
    font-size: 16px; line-height: 24px; padding-top: 12px; letter-spacing: 0.5px;
  }
  .plan {
    position: absolute; left: 14px; top: 1040px; width: 681px; height: 94px;
    background: var(--blue); color: var(--paper); text-align: center;
    font-size: 16px; line-height: 23.5px; padding-top: 2px; letter-spacing: 1.5px;
  }
  .source {
    position: absolute; left: 18px; top: 1146px; width: 674px; height: 41px;
    background: var(--ink); color: var(--paper); text-align: center;
    font-size: 15px; line-height: 41px; letter-spacing: 1.5px;
  }
</style>
</head>
<body>
<main class="poster">
  <header class="title-band">
    <span class="virus-icon white-left" role="img" aria-label="White virus illustration"></span>
    <span class="virus-icon white-right" role="img" aria-label="White virus illustration"></span>
    <span class="virus-icon yellow-right" role="img" aria-label="Yellow outlined virus illustration"></span>
    <h1 class="title">Fatigued and Overloaded<br>by COVID Messages</h1>
  </header>

  <h2 class="section-label">Participants Responded</h2>

  <div class="figure-art" role="img" aria-label="Illustration of a weary person turning away from a phone full of messages"></div>

  <section class="stat">
    <div class="bar red-track" style="left:264px; top:270px; width:349px;">
      <div class="fill" style="width:56%;"><span class="percent">55%</span></div><div class="rest"></div>
    </div>
    <p class="stat-label" style="left:264px; top:322px; width:349px;">Feel exhausted<br>by all the messages</p>
  </section>

  <section class="stat">
    <div class="bar blue-track" style="left:91px; top:443px; width:347px;">
      <div class="fill" style="width:56%;"><span class="percent">54%</span></div><div class="rest"></div>
    </div>
    <p class="stat-label" style="left:40px; top:495px; width:450px;">Feel overloaded by<br>the amount of information</p>
  </section>

  <section class="stat">
    <div class="bar red-track" style="left:264px; top:605px; width:349px;">
      <div class="fill" style="width:52%;"><span class="percent">51%</span></div><div class="rest"></div>
    </div>
    <p class="stat-label" style="left:240px; top:657px; width:400px;">Feel that the<br>messages are repetitive</p>
  </section>

  <section class="stat">
    <div class="bar blue-track" style="left:91px; top:779px; width:347px;">
      <div class="fill" style="width:68%;"><span class="percent">47%</span></div><div class="rest"></div>
    </div>
    <p class="stat-label" style="left:40px; top:831px; width:450px;">Feel like messages<br>exaggerate how bad it is</p>
  </section>

  <p class="summary">In other words, almost half of U.S. adults<br>show signs of message fatigue, information overload,<br>perceived message repetition, and perceived message exaggeration</p>

  <p class="plan">We will continue to survey 400 adults every week for<br>the next 16 weeks. Each time we will measure message fatigue,<br>information overload, perceived repetition, and perceived<br>exaggeration. We expect that it will increase over time</p>

  <footer class="source">This survey is based on U.S. adults from March 20th - 24th, 2020</footer>
</main>
</body>
</html>
```